Palu Sales Pipeline

We need an infographic to help the sales team understand the importance of a sales pipeline and how to grow and manage it. It's important that they understand every process plays a vital part and a complete circle. If you break one part, the sales process can be a failure.

Font styles to use
Serif

Colors
33b8a4
abd037

Requirements
Must have
• Have fun!
Nice to have
• Open to all ideas. Keep in mind that we are eastern philosophy focused!
Should not have
• Not applicable! Just have phone

```html
<!DOCTYPE html>
<html lang="en">
<head>
<meta charset="utf-8">
<title>PALU Pipeline</title>
<link href="https://fonts.googleapis.com/css2?family=Montserrat:wght@400;500;600;700&display=swap" rel="stylesheet">
<style>
  :root {
    --teal: #33b8a4;
    --lime: #abd037;
    --panel-left: #f2f4f3;
    --panel-right: #ebebeb;
    --box-border: #d6d6d6;
    --box-fill: #f7f7f7;
    --ink: #5f6062;
    --ink-strong: #555659;
    --rail: #c9c9c9;
  }
  * { margin: 0; padding: 0; box-sizing: border-box; }
  html, body { width: 1200px; height: 730px; overflow: hidden; }
  body { font-family: "Montserrat", sans-serif; color: var(--ink); }
  .canvas { position: relative; width: 1200px; height: 730px; background: var(--panel-right); }
  .diagram-panel { position: absolute; left: 0; top: 0; width: 634px; height: 730px; background: var(--panel-left); }
  .title-pill {
    position: absolute; left: 139px; top: 37px; width: 351px; height: 58px;
    border-radius: 29px; background: linear-gradient(90deg, #b4d44a, var(--lime));
    color: #fff; font-weight: 700; font-size: 34px; display: flex; align-items: center; justify-content: center;
  }
  .cycle { position: absolute; left: 0; top: 0; }
  .enso {
    position: absolute; left: 199px; top: 281px; width: 230px; height: 230px; border-radius: 50%;
    background: radial-gradient(circle, transparent 0 52%, var(--lime) 54% 72%, rgba(171,208,55,0) 74%);
  }
  .stage {
    position: absolute; width: 139px; height: 60px; background: var(--box-fill);
    border: 8px solid var(--box-border); display: flex; align-items: center; justify-content: center;
    text-align: center; font-weight: 700; font-size: 14px; line-height: 1.15; color: var(--ink);
  }
  .stage-engagement { left: 73px; top: 236px; }
  .stage-peak { left: 398px; top: 236px; }
  .stage-retention { left: 442px; top: 429px; }
  .stage-nurture { left: 39px; top: 429px; }
  .stage-collection { left: 239px; top: 545px; }
  .step-label { position: absolute; color: var(--teal); font-weight: 700; font-size: 18px; white-space: nowrap; transform: translate(-50%, -50%); }
  .step-package { left: 321px; top: 180px; }
  .step-closure { left: 542px; top: 360px; }
  .step-seed { left: 496px; top: 558px; }
  .step-water { left: 145px; top: 558px; }
  .step-harvest { left: 75px; top: 360px; }
  .step-leads { left: 403px; top: 669px; transform: translateY(-50%); }

  .summary { position: absolute; left: 700px; top: 160px; width: 470px; }
  .summary-marker { position: absolute; left: 0; top: 7px; width: 0; height: 0;
    border-top: 22px solid transparent; border-bottom: 22px solid transparent; border-right: 27px solid var(--lime); }
  .summary-intro { margin-left: 50px; font-size: 22px; line-height: 30px; color: var(--ink); }
  .summary-intro strong { font-weight: 700; color: var(--ink-strong); }
  .focus-heading { margin: 42px 0 0 50px; font-weight: 700; font-size: 17px; color: var(--ink-strong); }
  .focus-list { list-style: none; position: relative; margin: 28px 0 0 50px; }
  .focus-list::before { content: ""; position: absolute; left: 3px; top: 10px; bottom: 10px; width: 2px; background: var(--rail); }
  .focus-list li { position: relative; padding-left: 32px; font-size: 17px; line-height: 21px; height: 51px; }
  .focus-list li::before { content: ""; position: absolute; left: -3px; top: 2px; width: 14px; height: 14px; border-radius: 50%; background: var(--lime); }
</style>
</head>
<body>
<main class="canvas">
  <section class="diagram-panel">
    <div class="title-pill">PALU Pipeline</div>

    <div class="enso" role="img" aria-label="Green brush-stroke ensō circle at the centre of the cycle"></div>

    <svg class="cycle" width="634" height="730" viewBox="0 0 634 730" aria-hidden="true">
      <circle cx="311" cy="397" r="166" fill="none" stroke="var(--teal)" stroke-width="18"/>
      <g fill="var(--teal)">
        <polygon points="-18,-10 18,-10 0,16" transform="rotate(-86 311 397) translate(477 397)"/>
        <polygon points="-18,-10 18,-10 0,16" transform="rotate(-13 311 397) translate(477 397)"/>
        <polygon points="-18,-10 18,-10 0,16" transform="rotate(61 311 397) translate(477 397)"/>
        <polygon points="-18,-10 18,-10 0,16" transform="rotate(131 311 397) translate(477 397)"/>
        <polygon points="-18,-10 18,-10 0,16" transform="rotate(205 311 397) translate(477 397)"/>
      </g>
      <path d="M309 626 V663 H385" fill="none" stroke="var(--teal)" stroke-width="11" stroke-linecap="round" stroke-linejoin="round"/>
      <polygon points="294,632 324,632 309,612" fill="var(--teal)"/>
    </svg>

    <div class="stage stage-engagement">Engagement<br>Cycle</div>
    <div class="stage stage-peak">Peak Cycle</div>
    <div class="stage stage-retention">Retention</div>
    <div class="stage stage-nurture">Nurture<br>Rapport</div>
    <div class="stage stage-collection">Collection<br>Build-up</div>

    <span class="step-label step-package">Package/Present</span>
    <span class="step-label step-closure">Closure</span>
    <span class="step-label step-seed">Seed/Plant</span>
    <span class="step-label step-water">Water/Sun</span>
    <span class="step-label step-harvest">Harvest</span>
    <span class="step-label step-leads">Lead Sources</span>
  </section>

  <section class="summary">
    <span class="summary-marker"></span>
    <p class="summary-intro"><strong>PALU Sales Pipeline</strong> focuses on the understanding of the Subject Life Cycle</p>
    <h2 class="focus-heading">Mastering Five Key Focuses:</h2>
    <ul class="focus-list">
      <li>Collection/Build-up (Seed)</li>
      <li>Nurture/Rapport (Water/Sun)</li>
      <li>Engagement (Harvest/Prune)</li>
      <li>Peak/Summit (Package/Presentation)</li>
      <li>Retention/Descent (Plant)</li>
    </ul>
  </section>
</main>
</body>
</html>
```